PTA Business Card

Seeking design for a business card, standard size. It is going to be for myself in regards to PTA - details:

Hollis Fernway Elementary School
PTA President
Neil Brawley
555-208-3147
Brawl1984@mailnest.example

Requirement:
Facebook icon? "Hollis Fernway PTA Durn"
Twitter thing? I am new to twitter so not sure what to put, here is the link:
https://twitter.com/HFRoverbirdsPTA

I was thinking on the front would be a notebook paper background? Not a requirement but was thinking it would look cool?

Total freedom here, let your creativity spread because I don't have any suggestions for design, sorry. Colors of school district are black and yellow.

Backside I am not sure exactly what to put on it.

```html
<!DOCTYPE html>
<html lang="en">
<head>
<meta charset="utf-8">
<title>PTA Business Card – Front and Back</title>
<link rel="stylesheet" href="https://fonts.googleapis.com/css2?family=Nunito+Sans:wght@400;600;800&display=swap">
<style>
  :root {
    --backdrop: #262626;
    --kraft: #c8b396;
    --kraft-edge: #b39e82;
    --school-yellow: #ffe000;
    --ink: #1c1c1c;
    --paper-white: #ffffff;
  }
  * { box-sizing: border-box; margin: 0; padding: 0; }
  html, body {
    width: 840px; height: 1200px; overflow: hidden;
    background: var(--backdrop);
    font-family: "Nunito Sans", sans-serif;
    color: var(--ink);
  }
  .canvas { position: relative; width: 840px; height: 1200px; }
  .card {
    position: absolute; top: 351px;
    width: 302px; height: 498px;
    background: var(--kraft);
    border: 1px solid var(--kraft-edge);
    overflow: hidden;
  }
  .card--front { left: 104px; }
  .card--back { left: 433px; }

  /* Front */
  .title-block {
    position: absolute; left: 76px; top: 47px;
    width: 226px; height: 225px;
    background: var(--school-yellow);
  }
  .school-name {
    position: absolute; left: 56px; top: 95px;
    font-weight: 800; font-size: 28px; line-height: 40px;
    letter-spacing: 0.6px; white-space: nowrap;
  }
  .holder { position: absolute; left: 56px; top: 356px; }
  .holder-name { font-weight: 600; font-size: 28px; line-height: 34px; white-space: nowrap; }
  .holder-role { font-size: 17px; line-height: 20px; }
  .holder-role .highlight {
    background: var(--ink); color: var(--paper-white);
    padding: 0 3px;
  }

  /* Back */
  .contact-row {
    position: absolute; left: 47px; right: 0; height: 34px;
    border-bottom: 2px solid var(--ink);
    display: flex; align-items: center;
  }
  .contact-row--phone { top: 112px; }
  .contact-row--email { top: 162px; }
  .contact-icon {
    width: 32px; height: 32px; background: var(--ink);
    display: flex; align-items: center; justify-content: center;
    flex: none;
  }
  .contact-text { margin-left: 9px; font-size: 19px; white-space: nowrap; }
  .contact-row--email .contact-text { font-size: 14px; letter-spacing: -0.1px; }

  .follow-label {
    position: absolute; left: 47px; top: 299px;
    font-size: 19px; font-weight: 600;
  }
  .social-row {
    position: absolute; left: 47px; right: 0; height: 32px;
    display: flex; align-items: stretch;
  }
  .social-row--first { top: 329px; }
  .social-row--second { top: 366px; }
  .social-marker {
    width: 32px; background: var(--ink); flex: none;
    display: flex; align-items: center; justify-content: center;
  }
  .social-marker span {
    width: 12px; height: 12px; background: var(--school-yellow);
  }
  .social-band {
    flex: 1; background: var(--school-yellow);
    display: flex; align-items: center;
    padding-left: 9px; font-size: 17px; white-space: nowrap;
  }
</style>
</head>
<body>
<main class="canvas">
  <section class="card card--front" aria-label="Card front">
    <div class="title-block"></div>
    <h1 class="school-name">Hollis Fernway<br>Elementary<br>School</h1>
    <div class="holder">
      <p class="holder-name">Neil Brawley</p>
      <p class="holder-role">PTA <span class="highlight">President</span></p>
    </div>
  </section>

  <section class="card card--back" aria-label="Card back">
    <div class="contact-row contact-row--phone">
      <div class="contact-icon">
        <svg width="16" height="22" viewBox="0 0 16 22" aria-hidden="true">
          <rect x="1" y="1" width="14" height="20" rx="2" fill="var(--school-yellow)"/>
          <rect x="3" y="3" width="10" height="7" fill="var(--ink)"/>
          <g fill="var(--ink)">
            <rect x="3" y="12" width="2.5" height="2"/><rect x="6.75" y="12" width="2.5" height="2"/><rect x="10.5" y="12" width="2.5" height="2"/>
            <rect x="3" y="15.5" width="2.5" height="2"/><rect x="6.75" y="15.5" width="2.5" height="2"/><rect x="10.5" y="15.5" width="2.5" height="2"/>
          </g>
        </svg>
      </div>
      <span class="contact-text">555-208-3147</span>
    </div>
    <div class="contact-row contact-row--email">
      <div class="contact-icon">
        <svg width="22" height="15" viewBox="0 0 22 15" aria-hidden="true">
          <rect x="0" y="0" width="22" height="15" fill="var(--school-yellow)"/>
          <polyline points="0,0 11,9 22,0" fill="none" stroke="var(--ink)" stroke-width="1.6"/>
        </svg>
      </div>
      <span class="contact-text">Brawl1984@mailnest.example</span>
    </div>

    <p class="follow-label">FOLLOW US:</p>
    <div class="social-row social-row--first">
      <div class="social-marker"><span></span></div>
      <div class="social-band">HFRoverbirdsPTA</div>
    </div>
    <div class="social-row social-row--second">
      <div class="social-marker"><span></span></div>
      <div class="social-band">Hollis Fernway PTA Durn</div>
    </div>
  </section>
</main>
</body>
</html>
```